Toravelle Works Luxury Candles

Luxury box design,, simple and sophisticated look,,

My collection of candles come in 5 different fragrances, i would like to be able to change the fragrance name on the boxes,,,,

I would like the outline of australia on the front down the bottom , (only small) to represent this is an australian product.

My boxes are white gloss,,,

Happy for you to use my current logo ,,, however you'll have to change Toravelle Nails to Toravelle Works.

```html
<!DOCTYPE html>
<html lang="en">
<head>
<meta charset="utf-8">
<title>Toravelle Works Luxury Candles – Box Panels</title>
<link rel="stylesheet" href="https://fonts.googleapis.com/css2?family=Cormorant+Garamond:ital,wght@0,400;0,500;1,400&family=Cinzel:wght@400&display=swap">
<style>
  :root {
    --page: #ffffff;
    --ink: #1f1a10;
    --sand: #ded6ac;
    --butter: #ece2a6;
    --cream: #f4f1e4;
    --sage: #c4bd98;
    --sage-deep: #b3ac87;
    --gold-dark: #94702e;
    --gold-mid: #c6a24a;
    --gold-light: #f0e592;
    --gold-edge: #f6e98a;
    --badge: #b7b4ac;
  }
  * { margin: 0; padding: 0; box-sizing: border-box; }
  html, body { width: 1200px; height: 827px; overflow: hidden; background: var(--page); }
  .canvas { position: relative; width: 1200px; height: 827px; }

  .box-panel {
    position: absolute; top: 72px; width: 456px; height: 670px; overflow: hidden;
  }
  .box-panel--front { left: 94px; }
  .box-panel--back { left: 654px; }

  .panel-texture {
    position: absolute; inset: 0;
    background:
      radial-gradient(ellipse 40% 30% at 30% 40%, rgba(240,230,160,0.45), transparent 70%),
      linear-gradient(90deg, var(--sand) 0%, var(--butter) 40%, var(--cream) 60%, var(--sage) 72%, var(--sage-deep) 82%, var(--cream) 93%, #faf9f3 100%);
  }

  .brand-band {
    position: absolute; left: 0; right: 0; top: 288px; height: 144px;
    background: linear-gradient(90deg, var(--gold-dark) 0%, var(--gold-mid) 30%, var(--gold-light) 55%, var(--gold-mid) 78%, var(--gold-dark) 100%);
    border-top: 4px solid var(--gold-edge);
    border-bottom: 4px solid var(--gold-edge);
    text-align: center; color: var(--ink);
  }
  .brand-name {
    font-family: "Cormorant Garamond", serif; font-weight: 500;
    font-size: 50px; line-height: 1; margin-top: 32px; letter-spacing: 1px;
  }
  .brand-tagline {
    font-family: "Cinzel", serif; font-size: 15px; letter-spacing: 7px; margin-top: 18px;
  }

  .fragrance {
    position: absolute; font-family: "Cinzel", serif; font-size: 12px;
    letter-spacing: 4px; color: var(--ink);
  }
  .box-panel--front .fragrance { left: 30px; top: 697px; top: 625px; }

  .origin-badge {
    position: absolute; left: 394px; top: 618px; width: 44px; height: 34px;
  }

  .back-brand { position: absolute; left: 48px; top: 176px; width: 220px; text-align: center; color: var(--ink); }
  .back-brand .brand-name { font-size: 28px; margin-top: 0; }
  .back-brand .brand-tagline { font-size: 8px; letter-spacing: 3px; margin-top: 8px; }
  .box-panel--back .fragrance { left: 48px; top: 240px; }

  .description {
    position: absolute; left: 48px; top: 266px; width: 260px;
    font-family: "Cormorant Garamond", serif; font-style: italic;
    font-size: 12.5px; line-height: 29.5px; color: var(--ink); letter-spacing: -0.2px;
  }
</style>
</head>
<body>
<main class="canvas">

  <section class="box-panel box-panel--front" aria-label="Box front">
    <div class="panel-texture" role="img" aria-label="Soft watercolour wash in sand, butter yellow, cream and sage tones"></div>
    <div class="brand-band">
      <p class="brand-name">Toravelle Works</p>
      <p class="brand-tagline">LUXURY CANDLES</p>
    </div>
    <p class="fragrance">COTTON CANDY</p>
    <svg class="origin-badge" viewBox="0 0 44 34" role="img" aria-label="Small product of Australia outline mark">
      <ellipse cx="22" cy="17" rx="21" ry="16" fill="var(--badge)"/>
    </svg>
  </section>

  <section class="box-panel box-panel--back" aria-label="Box back">
    <div class="panel-texture" role="img" aria-label="Soft watercolour wash in sand, butter yellow, cream and sage tones"></div>
    <div class="back-brand">
      <p class="brand-name">Toravelle Works</p>
      <p class="brand-tagline">LUXURY CANDLES</p>
    </div>
    <p class="fragrance">COTTON CANDY</p>
    <p class="description">
      Lorem ipsum dolor sit amet, consectetur adipiscing elit.<br>
      Vestibulum efficitur lobortis orci ac consequat. Ut porta<br>
      pellentesque metus, sit amet tristique turpis ornare in. Ut<br>
      dignissim ligula nisi, vitae mollis lacus mollis semper.<br>
      Nulla tincidunt porttitor nisi eget luctus. Vestibulum<br>
      efficitur fringilla enim id vehicula. Proin suscipit, diam nec<br>
      bibendum ullamcorper, odio quam gravida libero, vel<br>
      tristique nisi turpis id purus. Phasellus ac tincidunt<br>
      magna. Sed scelerisque interdum magna ut tempor.
    </p>
  </section>

</main>
</body>
</html>
```